Whitening Pen artwork design

Whitening Pens with silkscreen printing:
sample: https://www.shopmarrow.example/Toviqa-Whitening-Carbamide-Sensitivity-Travel-Friendly/dp/K93R4T8W1Q/ref=sr_1_5?dchild=1&keywords=whitening+pen&qid=1728301944&sr=8-5

inside the writing:
"teeth whitening pen " change to "BRISK WHITENING PEN"
"logo" change to our logo

requirements:
Inches: 1.77" wide x 1.57" around
CM: 4.5cm wide x 4cm around

See attached file Generic Pen Artwork Placement Silkscreen – this is not a template, just a guideline, refer to the exact sizing above

- An "identifying marker" is required: Teeth Whitening Pen or Teeth Whitening Gel (for example)

-We require PDF files created to print ready specifications. Color images should be down-sampled to 300DPI

-Please provide us your Hueledger color reference for the color used in your artwork

https://www.hueledger.example/color-finder#/pick?swatchBook=solidCoatedV3M2

-Please ensure that all fonts are embedded in the PDF document or make sure you convert fonts to outlines to prevent any issues with fonts (AI-Type-Create Outlines)

We will need your print ready artwork in a high resolution PDF file

```html
<!DOCTYPE html>
<html lang="en">
<head>
<meta charset="utf-8">
<title>BRISK Whitening Pen – Label Artwork</title>
<link rel="stylesheet" href="https://fonts.googleapis.com/css2?family=Jost:wght@300;600&display=swap">
<style>
  :root {
    --canvas-bg: #ececec;
    --label-light: #f5ad9e;
    --label-dark: #ec9585;
    --ink-white: #ffffff;
  }
  html, body {
    margin: 0;
    padding: 0;
    width: 1200px;
    height: 900px;
    overflow: hidden;
    background: var(--canvas-bg);
  }
  .artboard {
    position: relative;
    width: 1200px;
    height: 900px;
  }
  .pen-label {
    position: absolute;
    left: 506px;
    top: 46px;
    width: 188px;
    height: 808px;
    display: block;
  }
  .product-name {
    font-family: "Jost", sans-serif;
    font-weight: 300;
    font-size: 112px;
    fill: var(--ink-white);
  }
  .identifier {
    font-family: "Jost", sans-serif;
    font-weight: 300;
    font-size: 54px;
    fill: var(--ink-white);
  }
  .brand-name {
    font-family: "Jost", sans-serif;
    font-weight: 600;
    font-size: 54px;
    letter-spacing: 4px;
    fill: var(--ink-white);
  }
  .brand-dot {
    fill: var(--ink-white);
  }
</style>
</head>
<body>
  <main class="artboard">
    <svg class="pen-label" viewBox="0 0 188 808" xmlns="http://www.w3.org/2000/svg" aria-label="BRISK whitening pen label">
      <defs>
        <linearGradient id="labelTone" x1="0" y1="0" x2="1" y2="0">
          <stop offset="0" stop-color="var(--label-light)"/>
          <stop offset="1" stop-color="var(--label-dark)"/>
        </linearGradient>
      </defs>
      <rect class="label-band" x="0" y="0" width="188" height="808" fill="url(#labelTone)"/>

      <text class="product-name" transform="translate(22 40) rotate(90)">BRISK</text>
      <text class="identifier" transform="translate(42 324) rotate(90)">WHITENING PEN</text>

      <circle class="brand-dot" cx="136" cy="232" r="12"/>
      <text class="brand-name" transform="translate(116 262) rotate(90)">SOLVEN</text>
    </svg>
  </main>
</body>
</html>
```